Proposal Poster, posters for kids to hold

I am proposing to my girlfriend soon, I need two posters made for my kids to hold one I want to say “be my mommy”
And the other “will you marry my daddy”
Both in horizontal format. I plan on sending the files to a print shop to get them printed on a large poster. Simple is fine with maybe a few graphics. Open to anything. Kids will be holding it from the beach as we are on a jet ski close to shore. Must be readable font from a short distance

• Cute but readable font from a distance

```html
<!DOCTYPE html>
<html lang="en">
<head>
<meta charset="utf-8">
<title>Will You Marry My Daddy – Proposal Poster</title>
<link rel="stylesheet" href="https://fonts.googleapis.com/css2?family=Abril+Fatface&family=Gochi+Hand&display=swap">
<style>
  :root {
    --paper-top: #fcedc8;
    --paper-bottom: #fcf8d9;
    --ink: #0d0d0d;
    --bloom-lilac: #a7aee6;
    --bloom-blush: #efdcd6;
    --leaf-sage: #b7ad86;
    --ring-gold-light: #ffd24a;
    --ring-gold-deep: #f59a1f;
  }
  * { margin: 0; padding: 0; box-sizing: border-box; }
  html, body {
    width: 1200px;
    height: 776px;
    overflow: hidden;
  }
  .poster {
    position: relative;
    width: 1200px;
    height: 776px;
    background: linear-gradient(180deg, var(--paper-top) 0%, var(--paper-bottom) 70%);
    color: var(--ink);
    overflow: hidden;
  }
  .headline {
    position: absolute;
    left: 0;
    right: 0;
    text-align: center;
  }
  .headline--lead {
    top: 112px;
    font-family: "Gochi Hand", cursive;
    font-size: 168px;
    line-height: 1;
    letter-spacing: 2px;
  }
  .headline--key {
    top: 268px;
    font-family: "Abril Fatface", serif;
    font-size: 244px;
    line-height: 1;
    letter-spacing: 6px;
  }
  .headline--close {
    top: 500px;
    font-family: "Gochi Hand", cursive;
    font-size: 168px;
    line-height: 1;
    letter-spacing: 2px;
  }
  .floral-spray {
    position: absolute;
    width: 184px;
    height: 148px;
    border-radius: 50%;
    background: radial-gradient(circle at 55% 50%, var(--bloom-blush) 0%, var(--bloom-lilac) 38%, var(--leaf-sage) 62%, rgba(183,173,134,0) 72%);
  }
  .floral-spray--top-left { left: 48px; top: 38px; }
  .floral-spray--bottom-right { left: 964px; top: 588px; }
  .ring-pair {
    position: absolute;
    width: 80px;
    height: 80px;
    border-radius: 40%;
    background: linear-gradient(135deg, var(--ring-gold-light), var(--ring-gold-deep));
    opacity: 0.85;
  }
  .ring-pair--top-right { left: 1061px; top: 51px; }
  .ring-pair--bottom-left { left: 59px; top: 642px; }
</style>
</head>
<body>
  <main class="poster">
    <div class="floral-spray floral-spray--top-left" role="img" aria-label="Bouquet of lilac and blush anemones with sage leaves"></div>
    <div class="ring-pair ring-pair--top-right" role="img" aria-label="Pair of interlocking gold wedding rings"></div>

    <h1 class="headline headline--lead">will you</h1>
    <p class="headline headline--key">MARRY</p>
    <p class="headline headline--close">my daddy?</p>

    <div class="ring-pair ring-pair--bottom-left" role="img" aria-label="Pair of interlocking gold wedding rings"></div>
    <div class="floral-spray floral-spray--bottom-right" role="img" aria-label="Bouquet of blush and lilac anemones with sage leaves"></div>
  </main>
</body>
</html>
```